Web Developer Needs a Business Card Design

I need a personal business card design that represents me as a web developer for potential employers. I would like the background to be a dark color on the front for contrast with my logo and name. The back will have all my information along with a smaller version of the logo. I want something with a modern look and feel, not too conservative. This will be used for potential employers and freelance work.

Industry/Entity Type

Business

Contact Information for Business Card

Front should have my logo and name. The back should have all my personal information which would include: name: Tom Brevardi, phone: 570-614-9083, email: tombrevardi@mailwisp.com, website url: www.tombrevardi.com, logo, web developer.

Font styles to use
Sans Serif

Requirements
Must have
• Must include my logo. The color palette base color will be the logo color.

```html
<!DOCTYPE html>
<html lang="en">
<head>
<meta charset="utf-8">
<title>Tom Brevardi – Web Developer Business Card</title>
<link rel="stylesheet" href="https://fonts.googleapis.com/css2?family=PT+Serif:wght@400;700&display=swap">
<style>
  :root {
    --teal: #5fd8c2;
    --teal-deep: #44c3ab;
    --teal-light: #74e2cf;
    --paper: #ffffff;
    --paper-shade: #eef0f0;
    --ink: #5a5f63;
    --stage: #e7e9ea;
  }
  * { box-sizing: border-box; margin: 0; padding: 0; }
  html, body {
    width: 1200px; height: 1062px; overflow: hidden;
    background: var(--stage);
    font-family: "PT Serif", Georgia, serif;
  }
  .canvas { position: relative; width: 1200px; height: 1062px; }

  .card {
    position: absolute; width: 640px; height: 366px;
    border-radius: 4px;
    box-shadow: 0 10px 28px rgba(0,0,0,.18);
    overflow: hidden;
  }

  /* Contact side */
  .card--contact {
    left: 80px; top: 100px;
    background: linear-gradient(135deg, var(--paper) 0%, var(--paper-shade) 100%);
  }
  .card--contact .side-band {
    position: absolute; right: 0; top: 0; bottom: 0; width: 62px;
    background: var(--teal);
  }
  .brand-mark {
    position: absolute; left: 70px; top: 92px;
    width: 170px; height: 170px; border-radius: 50%;
    border: 7px solid var(--teal);
    display: flex; align-items: center; justify-content: center;
  }
  .brand-mark__name {
    color: var(--teal); font-weight: 700; font-size: 22px; text-align: center; line-height: 1.15;
  }
  .role {
    position: absolute; left: 78px; top: 292px;
    color: var(--teal); font-size: 26px;
  }
  .divider {
    position: absolute; left: 300px; top: 96px; width: 1px; height: 150px;
    background: linear-gradient(var(--paper), var(--teal), var(--paper));
  }
  .identity { position: absolute; left: 330px; top: 70px; }
  .identity__name { color: var(--teal); font-weight: 700; font-size: 28px; }
  .identity__title { color: var(--ink); font-size: 17px; margin-top: 4px; }
  .contacts { position: absolute; left: 330px; top: 160px; list-style: none; }
  .contacts li {
    display: flex; align-items: center; gap: 10px;
    color: var(--ink); font-size: 16px; margin-bottom: 12px;
  }
  .contacts svg { width: 16px; height: 16px; flex: none; }

  /* Brand side */
  .card--brand {
    left: 480px; top: 590px;
    background: linear-gradient(135deg, var(--teal-light) 0%, var(--teal) 55%, var(--teal-deep) 100%);
  }
  .brand-ring {
    position: absolute; left: 70px; top: 48px;
    width: 270px; height: 270px; border-radius: 50%;
    border: 16px solid var(--paper);
    display: flex; align-items: center; justify-content: center;
  }
  .brand-ring__name {
    color: var(--paper); font-weight: 700; font-size: 34px; text-align: center; line-height: 1.15;
  }
  .card--brand .role {
    left: 380px; top: 236px; color: var(--paper); font-size: 34px;
  }
</style>
</head>
<body>
<main class="canvas">
  <section class="card card--contact" aria-label="Contact side of business card">
    <div class="brand-mark"><span class="brand-mark__name">Tom<br>Brevardi</span></div>
    <p class="role">Web developer</p>
    <div class="divider"></div>
    <div class="identity">
      <h1 class="identity__name">Tom Brevardi</h1>
      <p class="identity__title">Manager</p>
    </div>
    <ul class="contacts">
      <li>
        <svg viewBox="0 0 16 16" aria-hidden="true"><path d="M4 1.5l2.2 3-1.4 1.6a8 8 0 0 0 5.1 5.1l1.6-1.4 3 2.2-1.3 2.3C7.5 14 2 8.5 1.7 2.8z" fill="var(--teal)"/></svg>
        570-614-9083
      </li>
      <li>
        <svg viewBox="0 0 16 16" aria-hidden="true" fill="none" stroke="var(--teal)" stroke-width="1.4"><circle cx="8" cy="8" r="6.5"/><ellipse cx="8" cy="8" rx="2.8" ry="6.5"/><path d="M1.5 8h13M2.5 4.8h11M2.5 11.2h11"/></svg>
        www.tombrevardi.com
      </li>
      <li>
        <svg viewBox="0 0 16 16" aria-hidden="true" fill="none" stroke="var(--teal)" stroke-width="1.6"><circle cx="8" cy="8" r="2.6"/><path d="M10.6 5.6v3.5c0 1.6 2.9 1.6 2.9-1.1A5.5 5.5 0 1 0 11 12.7"/></svg>
        tombrevardi@mailwisp.com
      </li>
    </ul>
    <div class="side-band"></div>
  </section>

  <section class="card card--brand" aria-label="Brand side of business card">
    <div class="brand-ring"><span class="brand-ring__name">Tom<br>Brevardi</span></div>
    <p class="role">Web developer</p>
  </section>
</main>
</body>
</html>
```